Web Design for a Travel Industry Company

i am Looking for a Web designer, that's makes me a template for our company in the Travel Sector. It must have a booking tool and a tool for queries. Pictures come from us. It must be simple so that we can then organize further. We plan a cover side, than in the top line, we want have buttons for choose. perfect will be a mix from the hotel Lindmoor homepage in Vienna and Kestlerfahrt.at. The site is already purchased and owned by us.
Updates

Ich brauche zusätzliche Tage um durchzusehen

Target Market(s)

Travel Industry / Luxury and GAY Peopele

Logo Text

see the Logos

Requirements
Must have
• is for gays. The design should be customized.
Nice to have
• For the website a booking tools. We can deliver pic from Vienna for the Web design.

```html
<!DOCTYPE html>
<html lang="en">
<head>
<meta charset="utf-8">
<title>Pride Roaming – Home</title>
<link rel="stylesheet" href="https://fonts.googleapis.com/css2?family=Archivo:wght@800&family=Roboto:wght@300;400;700&display=swap">
<style>
  :root{
    --ink:#555;
    --ink-dark:#3a3a3a;
    --navy:#2d3182;
    --nav-active:#5b79c5;
    --yellow:#e3cc47;
    --red:#d1323a;
    --green:#2f8a2b;
    --purple:#8c5ec9;
    --pink:#f1b6bb;
    --footer:#d9d9d9;
    --button:#666;
    --rule:#cfcfcf;
    --white:#fff;
  }
  *{box-sizing:border-box;margin:0;padding:0}
  html,body{width:1200px;height:2247px;overflow:hidden;background:var(--white)}
  body{font-family:"Roboto",Arial,sans-serif;color:var(--ink)}
  .page{position:relative;width:1200px;height:2247px;overflow:hidden}

  /* header */
  .brand{position:absolute;left:150px;top:31px;display:flex;align-items:center;gap:18px}
  .brand-mark{width:94px;height:94px;border-radius:50%;border:3px solid var(--navy);flex:none}
  .brand-name{font-family:"Roboto",Arial,sans-serif;font-weight:400;font-size:24px;color:var(--navy);white-space:nowrap}
  .main-nav{position:absolute;left:463px;top:66px;width:479px;height:27px;border-top:1px solid #666;border-bottom:1px solid #666;display:flex;font-size:11px;text-transform:uppercase;color:var(--navy)}
  .main-nav a{flex:1;display:flex;align-items:center;justify-content:center;color:inherit;text-decoration:none}
  .main-nav a.is-active{flex:0 0 87px;background:var(--nav-active);color:var(--white)}
  .user-tools{position:absolute;left:960px;top:65px;display:flex;align-items:center;gap:10px}

  /* hero */
  .hero{position:absolute;left:0;top:179px;width:1200px;height:346px;background:linear-gradient(180deg,#1a1410 0%,#3b2a20 40%,#2a3a40 70%,#2f6f7a 100%)}
  .hero-rule{position:absolute;height:2px;background:rgba(255,255,255,.85)}
  .hero-line{position:absolute;left:195px;height:46px;font-family:"Archivo",Arial,sans-serif;font-weight:800;font-size:46px;color:var(--white);letter-spacing:2px;line-height:46px;white-space:nowrap}
  .hero-line .bar{font-weight:400;opacity:.9;margin:0 8px}
  .hero-plane{position:absolute;left:800px;top:128px;width:64px;height:56px}

  /* categories */
  .category{position:absolute;top:550px;width:120px;text-align:center;font-size:16px;color:#666}
  .category-badge{display:block;width:70px;height:70px;border-radius:50%;margin:0 auto 20px}

  /* experience cards */
  .card{position:absolute;width:433px}
  .card-photo{height:165px}
  .card-meta{position:relative;height:62px}
  .card-icon{position:absolute;left:-4px;top:16px;width:34px;height:34px;border-radius:50%}
  .card-divider{position:absolute;left:40px;top:10px;height:46px;border-left:1px dashed #999}
  .card-title{position:absolute;left:52px;top:10px;font-size:16px;font-weight:300;text-transform:uppercase;color:var(--ink);white-space:nowrap}
  .card-rule{position:absolute;left:52px;right:0;top:31px;border-top:1px solid var(--rule)}
  .card-place{position:absolute;left:50px;top:43px;font-size:16px;font-weight:300;color:var(--ink)}
  .card-more{position:absolute;right:0;top:46px;width:147px;height:14px;background:var(--button);color:var(--white);font-size:9px;font-weight:700;text-align:center;line-height:14px}

  /* stories */
  .stories{position:absolute;left:0;top:1511px;width:1200px;height:519px;background:var(--pink)}
  .story{position:absolute;width:216px}
  .story-photo{position:absolute;left:2px;width:212px;height:212px;border-radius:50%;border:4px solid var(--white)}
  .story-box{position:absolute;left:0;top:196px;width:216px;background:var(--white);padding:14px 14px 28px;text-align:center}
  .story-title{font-size:26px;font-weight:400;color:var(--ink-dark);line-height:1.15}
  .story-sub{font-size:16px;font-weight:300;color:var(--ink-dark)}
  .story-rule{border-top:1px dashed #999;margin:14px 4px 16px}
  .story-text{text-align:left;font-size:12px;font-weight:300;line-height:15.7px;color:var(--ink-dark);padding:0 4px}

  /* footer */
  .site-footer{position:absolute;left:0;top:2030px;width:1200px;height:217px;background:var(--footer)}
  .footer-info{position:absolute;left:206px;font-size:10px;font-weight:700;color:var(--white);line-height:12px}
  .footer-rule{position:absolute;border-top:1px dashed #999}
  .footer-divider{position:absolute;top:37px;height:102px;border-left:1px solid #aaa}
  .field{position:absolute;background:var(--white);font-size:12px;color:#555;padding:11px 20px}
  .submit{position:absolute;left:442px;top:160px;width:295px;height:33px;background:#5c5c5c;color:var(--white);font-size:11px;font-weight:700;display:flex;align-items:center;justify-content:center}
  .footer-badge{position:absolute;top:37px;width:44px;height:44px;border-radius:50%;background:var(--purple);border:2px solid var(--white);display:flex;align-items:center;justify-content:center}
  .social-dot{position:absolute;top:113px;width:14px;height:14px;border-radius:50%;background:var(--white)}
</style>
</head>
<body>
<svg width="0" height="0" style="position:absolute" aria-hidden="true">
  <defs>
    <symbol id="icon-drink" viewBox="0 0 40 40">
      <g fill="none" stroke="#fff" stroke-width="1.6" stroke-linejoin="round">
        <rect x="10" y="14" width="7" height="20" rx="2"/>
        <path d="M12 14V7h3v7"/>
        <path d="M20 18h9l-1 7a3.5 3.5 0 0 1-7 0z"/>
        <path d="M24.5 29v5M21 34h7"/>
        <circle cx="29" cy="10" r="2"/><circle cx="32" cy="13" r="2"/><circle cx="28" cy="14" r="2"/>
      </g>
    </symbol>
    <symbol id="icon-relax" viewBox="0 0 40 40">
      <g fill="none" stroke="#fff" stroke-width="1.6" stroke-linejoin="round">
        <path d="M20 5c-7 0-11 5-11 11 0 6 6 10 8 14h6c2-4 8-8 8-14 0-6-4-11-11-11z"/>
        <path d="M20 5c-3 3-4 7-4 11s1 9 1 14M20 5c3 3 4 7 4 11s-1 9-1 14"/>
        <rect x="16" y="31" width="8" height="5" rx="1"/>
      </g>
    </symbol>
    <symbol id="icon-play" viewBox="0 0 40 40">
      <g fill="none" stroke="#fff" stroke-width="1.6" stroke-linejoin="round">
        <rect x="8" y="18" width="8" height="16"/>
        <rect x="16" y="8" width="10" height="26"/>
        <rect x="26" y="14" width="7" height="20"/>
        <path d="M19 12h4M19 16h4M19 20h4M19 24h4M10 22h4M10 26h4M28 18h3M28 22h3M6 34h29"/>
      </g>
    </symbol>
  </defs>
</svg>

<div class="page">

  <header class="site-header">
    <div class="brand">
      <span class="brand-mark"></span>
      <span class="brand-name">PRIDE ROAMING</span>
    </div>
    <nav class="main-nav">
      <a class="is-active" href="#">Home</a>
      <a href="#">About</a>
      <a href="#">Play</a>
      <a href="#">Relax</a>
      <a href="#">Book Online</a>
    </nav>
    <div class="user-tools">
      <svg width="18" height="20" viewBox="0 0 18 20" aria-label="Notifications"><path d="M9 2a5 5 0 0 1 5 5v5l2 3H2l2-3V7a5 5 0 0 1 5-5z" fill="#555"/><circle cx="9" cy="17.5" r="2" fill="#555"/></svg>
      <svg width="24" height="24" viewBox="0 0 24 24" aria-label="Account"><circle cx="12" cy="12" r="11" fill="#666"/><circle cx="12" cy="9.5" r="4" fill="#fff"/><path d="M4.5 19a9 6 0 0 1 15 0" fill="#fff"/></svg>
      <svg width="14" height="10" viewBox="0 0 14 10"><path d="M2 3l5 5 5-5" fill="none" stroke="#555" stroke-width="1.6"/></svg>
    </div>
  </header>

  <section class="hero" role="img" aria-label="Blurred evening bar interior in Vienna with warm lights and teal motion">
    <span class="hero-rule" style="left:195px;top:52px;width:405px"></span>
    <div class="hero-line" style="top:88px">LOSE<span class="bar">|</span>YOURSELF</div>
    <div class="hero-line" style="top:158px">DISCOVER<span class="bar">|</span>YOURSELF</div>
    <svg class="hero-plane" viewBox="0 0 64 60"><path d="M4 40l20-8 14-22c3-4 8-5 6 0L36 30l18 0 4-6h4l-3 10 1 10h-4l-3-5-18 2-6 16h-5l1-14-16 4z" fill="#fff"/></svg>
    <span class="hero-rule" style="left:195px;top:224px;width:572px"></span>
  </section>

  <div class="category" style="left:383px">
    <span class="category-badge" style="background:var(--yellow)"><svg width="70" height="70"><use href="#icon-drink" x="15" y="15" width="40" height="40"/></svg></span>DRINK
  </div>
  <div class="category" style="left:529px">
    <span class="category-badge" style="background:var(--red)"><svg width="70" height="70"><use href="#icon-relax" x="15" y="15" width="40" height="40"/></svg></span>RELAX
  </div>
  <div class="category" style="left:671px">
    <span class="category-badge" style="background:var(--green)"><svg width="70" height="70"><use href="#icon-play" x="15" y="15" width="40" height="40"/></svg></span>PLAY
  </div>

  <main class="experiences">
    <article class="card" style="left:151px;top:678px">
      <div class="card-photo" role="img" aria-label="Vienna skyline at dusk with a gothic cathedral spire" style="background:linear-gradient(180deg,#6d93b6 0%,#c9a49a 55%,#3a3a3c 100%)"></div>
      <div class="card-meta">
        <span class="card-icon" style="background:var(--yellow)"><svg width="34" height="34"><use href="#icon-drink" x="4" y="4" width="26" height="26"/></svg></span>
        <span class="card-divider"></span>
        <h3 class="card-title">Take a huge bite out of the Big Apple</h3>
        <span class="card-rule"></span>
        <p class="card-place">Austria, European</p>
        <span class="card-more">More Info</span>
      </div>
    </article>

    <article class="card" style="left:592px;top:678px">
      <div class="card-photo" role="img" aria-label="Subway platform with a train speeding past" style="background:linear-gradient(90deg,#4a4560 0%,#6b6478 35%,#7f95a8 65%,#a88a56 100%)"></div>
      <div class="card-meta">
        <span class="card-icon" style="background:var(--red)"><svg width="34" height="34"><use href="#icon-relax" x="4" y="4" width="26" height="26"/></svg></span>
        <span class="card-divider"></span>
        <h3 class="card-title">Swim &amp; divewith tiger sharks</h3>
        <span class="card-rule"></span>
        <p class="card-place">Austria, European</p>
        <span class="card-more">More Info</span>
      </div>
    </article>

    <article class="card" style="left:151px;top:957px">
      <div class="card-photo" role="img" aria-label="Baroque palace with formal gardens and fountains" style="background:linear-gradient(180deg,#b9a89a 0%,#6f8a5a 40%,#9aa89a 75%,#c4c0b8 100%)"></div>
      <div class="card-meta">
        <span class="card-icon" style="background:var(--green)"><svg width="34" height="34"><use href="#icon-play" x="4" y="4" width="26" height="26"/></svg></span>
        <span class="card-divider"></span>
        <h3 class="card-title">Detox &amp; rejuvenate in luxury</h3>
        <span class="card-rule"></span>
        <p class="card-place">Austria, European</p>
        <span class="card-more">More Info</span>
      </div>
    </article>

    <article class="card" style="left:595px;top:957px">
      <div class="card-photo" role="img" aria-label="Plated dessert with pink cream on a restaurant table" style="background:linear-gradient(135deg,#4a3a30 0%,#9a7a68 40%,#d8b0a8 60%,#5a4a40 100%)"></div>
      <div class="card-meta">
        <span class="card-icon" style="background:var(--yellow)"><svg width="34" height="34"><use href="#icon-drink" x="4" y="4" width="26" height="26"/></svg></span>
        <span class="card-divider"></span>
        <h3 class="card-title">Learn to cook in Austria</h3>
        <span class="card-rule"></span>
        <p class="card-place">Austria, France</p>
        <span class="card-more">More Info</span>
      </div>
    </article>

    <article class="card" style="left:151px;top:1223px">
      <div class="card-photo" style="height:168px;background:linear-gradient(90deg,#9aa6b0 0%,#6a8a4a 45%,#8a9ab8 75%,#b8b0a8 100%)" role="img" aria-label="Colourful apartment facade covered in greenery"></div>
      <div class="card-meta">
        <span class="card-icon" style="background:var(--red)"><svg width="34" height="34"><use href="#icon-relax" x="4" y="4" width="26" height="26"/></svg></span>
        <span class="card-divider"></span>
        <h3 class="card-title">Cycle through the city</h3>
        <span class="card-rule"></span>
        <p class="card-place">Austria, European</p>
        <span class="card-more">More Info</span>
      </div>
    </article>

    <article class="card" style="left:595px;top:1223px">
      <div class="card-photo" style="height:165px;background:linear-gradient(180deg,#1f6fd0 0%,#3a8ae0 100%)" role="img" aria-label="Giant Ferris wheel against a clear blue sky"></div>
      <div class="card-meta">
        <span class="card-icon" style="background:var(--green)"><svg width="34" height="34"><use href="#icon-play" x="4" y="4" width="26" height="26"/></svg></span>
        <span class="card-divider"></span>
        <h3 class="card-title">Explore European city</h3>
        <span class="card-rule"></span>
        <p class="card-place">Austria, European</p>
        <span class="card-more">More Info</span>
      </div>
    </article>
  </main>

  <section class="stories">
    <article class="story" style="left:203px;top:0">
      <div class="story-photo" role="img" aria-label="Rainbow flag waved in front of ancient arena arches" style="top:22px;background:linear-gradient(135deg,#b89a7a 0%,#d8c8b0 50%,#c86a8a 75%,#6a8ac8 100%)"></div>
      <div class="story-box">
        <h2 class="story-title">What You Need to Know</h2>
        <div class="story-rule"></div>
        <p class="story-text">Welcome to YOUR BUSINESS NAME, my very own passion project filled with unique and engaging content. Explore my site and all that I have to offer; perhaps YOUR BUSINESS NAME will ignite your own passions as well.</p>
      </div>
    </article>

    <article class="story" style="left:482px;top:0">
      <div class="story-photo" role="img" aria-label="Two glasses of red wine with snacks by a window" style="top:22px;background:linear-gradient(180deg,#4a6a3a 0%,#7a8a5a 40%,#8a2030 60%,#c8b8a8 100%)"></div>
      <div class="story-box">
        <h2 class="story-title">New<br>Culinary Tours</h2>
        <p class="story-sub">In the Wine Country</p>
        <div class="story-rule" style="margin-top:8px"></div>
        <p class="story-text">For years, I have served as a useful source to those seeking inspiration, help, or advice. I finally decided to own that role and be intentional about it. I started writing about my passions, my thoughts, and curious wonderings about our world.&nbsp; together.</p>
      </div>
    </article>

    <article class="story" style="left:761px;top:0">
      <div class="story-photo" role="img" aria-label="Horse-drawn carriage on a cobbled street" style="top:22px;background:linear-gradient(135deg,#c8c4c0 0%,#8a7a6a 45%,#5a4a3e 70%,#a8a4a0 100%)"></div>
      <div class="story-box">
        <h2 class="story-title">Harlan Vey<br>Ostrom</h2>
        <div class="story-rule"></div>
        <p class="story-text">We are all told, “live your life to the fullest”; I am here to do just that. YOUR BUSINESS NAME serves as a vessel to project my passions, and clue in my loyal readers as to what inspires me in this crazy world. So, sit back, relax, and read on.</p>
      </div>
    </article>
  </section>

  <footer class="site-footer">
    <p class="footer-info" style="top:40px">214 Morrow Lane<br>Vienna, AT 1010<br>hello@prideroam.at</p>
    <span class="footer-rule" style="left:209px;top:96px;width:188px"></span>
    <p class="footer-info" style="top:118px">© 2023 by PRIDEROAMING.<br>Proudly created with <u>Sitecrafter.com</u></p>
    <span class="footer-divider" style="left:421px"></span>

    <form class="contact-form">
      <div class="field" style="left:442px;top:35px;width:149px;height:37px">Name</div>
      <div class="field" style="left:442px;top:76px;width:149px;height:37px">Email</div>
      <div class="field" style="left:442px;top:118px;width:149px;height:37px">Subject</div>
      <div class="field" style="left:595px;top:35px;width:142px;height:120px">Message</div>
      <div class="submit">Submit</div>
    </form>

    <span class="footer-divider" style="left:764px"></span>
    <span class="footer-badge" style="left:786px"><svg width="30" height="30"><use href="#icon-drink" width="30" height="30"/></svg></span>
    <span class="footer-badge" style="left:857px"><svg width="30" height="30"><use href="#icon-play" width="30" height="30"/></svg></span>
    <span class="footer-badge" style="left:928px"><svg width="30" height="30"><use href="#icon-relax" width="30" height="30"/></svg></span>
    <span class="footer-rule" style="left:786px;top:96px;width:188px"></span>
    <span class="social-dot" style="left:859px"></span>
    <span class="social-dot" style="left:886px"></span>
  </footer>

</div>
</body>
</html>
```